VELDRAKE ORES
Project: VELDRAKE ORES
VELDRAKE ORES - Jewelry
Creative Brief
Modern
Tobias Marenko
Founder and Managing Director
Rua Fernao Lidamba No 318 2nd Floor Suite#7 Luanda, Angola
t.marenko@veldrake.com

```html
<!DOCTYPE html>
<html lang="en">
<head>
<meta charset="UTF-8">
<title>Veldrake Ores – Business Card</title>
<link rel="stylesheet" href="https://fonts.googleapis.com/css2?family=Open+Sans:wght@400;600;700&display=swap">
<style>
  :root {
    --stage: #2b2b2d;
    --gold-light: #f5d58e;
    --gold-mid: #d9a650;
    --gold-deep: #9a6a3a;
    --gold-text: #d99a2b;
    --ink: #1c1c1c;
    --grey-text: #6b6b6b;
    --band: #111111;
    --paper: #ffffff;
  }
  * { margin: 0; padding: 0; box-sizing: border-box; }
  html, body {
    width: 1200px; height: 900px; overflow: hidden;
    background: var(--stage);
    font-family: "Open Sans", sans-serif;
  }
  .canvas { position: relative; width: 1200px; height: 900px; }

  .card {
    position: absolute; left: 320px; width: 560px; height: 320px;
    box-shadow: 0 10px 30px rgba(0,0,0,.45);
    overflow: hidden;
  }

  /* Front */
  .card-front {
    top: 105px;
    background: linear-gradient(120deg, var(--gold-light) 0%, var(--gold-mid) 55%, var(--gold-deep) 100%);
  }
  .front-brand {
    position: absolute; left: 0; right: 0; top: 118px;
    display: flex; justify-content: center; align-items: center; gap: 12px;
  }
  .front-brand .mark { width: 22px; height: 22px; background: var(--ink); }
  .front-brand .name {
    font-size: 34px; font-weight: 700; color: var(--ink); letter-spacing: 2px;
  }
  .front-web {
    position: absolute; left: 0; right: 0; top: 238px; text-align: center;
    font-size: 12px; letter-spacing: 4px; color: #4a3a28;
  }

  /* Back */
  .card-back { top: 475px; background: var(--paper); }
  .back-brand {
    position: absolute; left: 48px; top: 88px;
    font-size: 30px; font-weight: 700; color: var(--ink); letter-spacing: 1px;
  }
  .band { position: absolute; left: 0; top: 150px; width: 380px; height: 80px; }
  .holder { position: absolute; left: 46px; top: 178px; }
  .holder .person { font-size: 17px; font-weight: 700; color: var(--gold-text); line-height: 1.2; }
  .holder .role { font-size: 13px; color: #ffffff; line-height: 1.4; }

  .contacts { position: absolute; left: 46px; top: 248px; list-style: none; }
  .contacts li {
    display: flex; align-items: center; gap: 8px;
    font-size: 12.5px; color: var(--grey-text); line-height: 19px;
  }
  .contacts svg { width: 12px; height: 12px; flex: none; }

  .address {
    position: absolute; right: 34px; top: 108px; text-align: right;
    font-size: 13px; line-height: 19px; color: var(--grey-text);
  }
</style>
</head>
<body>
<div class="canvas">

  <section class="card card-front" aria-label="Card front">
    <div class="front-brand">
      <span class="mark"></span>
      <span class="name">VELDRAKE ORES</span>
    </div>
    <p class="front-web">www.veldrake.com</p>
  </section>

  <section class="card card-back" aria-label="Card back">
    <div class="back-brand">VELDRAKE ORES</div>

    <svg class="band" viewBox="0 0 380 80" aria-hidden="true">
      <defs>
        <linearGradient id="stripe" x1="0" x2="1">
          <stop offset="0" stop-color="#f2c77a"/>
          <stop offset="1" stop-color="#a8703c"/>
        </linearGradient>
      </defs>
      <polygon points="0,22 300,22 250,80 0,80" fill="var(--band)"/>
      <polygon points="300,10 318,10 262,76 244,76" fill="url(#stripe)"/>
      <polygon points="324,10 336,10 282,76 270,76" fill="url(#stripe)"/>
      <polygon points="342,10 352,10 298,76 288,76" fill="url(#stripe)"/>
      <polygon points="290,10 300,10 300,22 288,22" fill="url(#stripe)"/>
      <rect x="280" y="10" width="80" height="4" fill="url(#stripe)"/>
    </svg>

    <div class="holder">
      <p class="person">Tobias Marenko</p>
      <p class="role">Founder &amp; Managing Director</p>
    </div>

    <ul class="contacts">
      <li>
        <svg viewBox="0 0 12 12"><rect x="3" y="0.5" width="6" height="11" rx="1" fill="none" stroke="var(--gold-text)" stroke-width="1.3"/></svg>
        924-518-207
      </li>
      <li>
        <svg viewBox="0 0 12 12"><rect x="0.5" y="2" width="11" height="8" fill="var(--gold-text)"/><polyline points="0.5,2 6,7 11.5,2" fill="none" stroke="#fff" stroke-width="1"/></svg>
        t.marenko@veldrake.com
      </li>
      <li>
        <svg viewBox="0 0 12 12"><circle cx="6" cy="6" r="5.2" fill="none" stroke="var(--gold-text)" stroke-width="1.2"/><ellipse cx="6" cy="6" rx="2.2" ry="5.2" fill="none" stroke="var(--gold-text)" stroke-width="1"/><line x1="0.8" y1="6" x2="11.2" y2="6" stroke="var(--gold-text)" stroke-width="1"/></svg>
        www.veldrake.com
      </li>
    </ul>

    <address class="address" style="font-style:normal">
      Rua Fernao Lidamba, No 318<br>
      2nd Floor Suite#7<br>
      Luanda, Angola
    </address>
  </section>

</div>
</body>
</html>
```